Property Development Business Cards

I need a business card design for Blue Harbour Developments Pty Ltd. We are a property development company in Australia and our name defines the five values that we adhere to, being Profitable, Partnerships, Quality Developments, Eco Friendly and Enduring Design.

I have attached the current logo that I use, it is just five yellow circles connected to a single cricle in the middle.

Target Market(s)

Our Target audience is real estate agents, owners of properties, builders and other trades

Industry/Entity Type

Business

Requirements
Must have
• Want to have two sides to the card, one with details and one to just highlight the company

```html
<!DOCTYPE html>
<html lang="en">
<head>
<meta charset="utf-8">
<title>Blue Harbour Developments – Business Cards</title>
<link rel="stylesheet" href="https://fonts.googleapis.com/css2?family=Mulish:wght@400;600;700&display=swap">
<style>
  :root {
    --stage: #000000;
    --card: #ffffff;
    --band: #8a8a8c;
    --ink: #2b2b2b;
    --ink-soft: #3c3c3c;
    --accent: #f39a1e;
    --accent-light: #ffd23a;
  }
  * { margin: 0; padding: 0; box-sizing: border-box; }
  html, body {
    width: 1200px;
    height: 900px;
    overflow: hidden;
    background: var(--stage);
    font-family: "Mulish", sans-serif;
  }
  .canvas {
    position: relative;
    width: 1200px;
    height: 900px;
  }
  .card {
    position: absolute;
    width: 504px;
    height: 286px;
    background: var(--card);
    border-radius: 16px;
    overflow: hidden;
  }

  /* Details side */
  .card--details { left: 136px; top: 132px; }
  .card__band {
    position: absolute;
    left: 0;
    width: 100%;
    height: 20px;
    background: var(--band);
  }
  .card__band--top { top: 0; }
  .card__band--bottom { bottom: 0; }
  .details-brand {
    position: absolute;
    left: 26px;
    top: 64px;
    display: flex;
    align-items: center;
    gap: 10px;
    font-size: 14px;
    font-weight: 600;
    color: var(--ink-soft);
  }
  .contact {
    position: absolute;
    right: 26px;
    top: 106px;
    text-align: right;
    font-size: 15.5px;
    line-height: 22px;
    color: var(--ink);
  }
  .contact__name {
    color: var(--accent);
    font-weight: 700;
    text-transform: uppercase;
    letter-spacing: 0.3px;
  }
  .contact__address { margin-top: 26px; }

  /* Brand side */
  .card--brand { left: 614px; top: 356px; }
  .brand-mark {
    position: absolute;
    left: 84px;
    top: 98px;
    color: var(--ink);
    font-weight: 700;
  }
  .brand-mark__name {
    font-size: 58px;
    line-height: 58px;
    letter-spacing: -1px;
  }
  .brand-mark__line {
    font-size: 29px;
    line-height: 32px;
    letter-spacing: 1px;
    text-transform: uppercase;
    padding-left: 6px;
  }
  .brand-mark__suffix {
    font-size: 11px;
    line-height: 14px;
    text-transform: uppercase;
    text-align: right;
  }
  .brand-dot {
    position: absolute;
    left: 380px;
    top: 42px;
  }
</style>
</head>
<body>
<main class="canvas">

  <section class="card card--details" aria-label="Business card, details side">
    <div class="card__band card__band--top"></div>
    <div class="details-brand">
      <svg width="28" height="28" viewBox="0 0 28 28" aria-hidden="true">
        <circle cx="14" cy="14" r="13" fill="var(--accent)"/>
      </svg>
      <span>Blue Harbour</span>
    </div>
    <address class="contact" style="font-style: normal;">
      <div class="contact__name">Daniel Mercer</div>
      <div class="contact__phone">Mobile: 0400 123 456</div>
      <div class="contact__email">Daniel@BlueHarbourDevelopments.com.au</div>
      <div class="contact__address">PO Box 218<br>Harrison, ACT 2914</div>
    </address>
    <div class="card__band card__band--bottom"></div>
  </section>

  <section class="card card--brand" aria-label="Business card, brand side">
    <svg class="brand-dot" width="52" height="52" viewBox="0 0 52 52" aria-hidden="true">
      <circle cx="26" cy="26" r="25" fill="var(--accent)"/>
    </svg>
    <div class="brand-mark">
      <div class="brand-mark__name">Blue Harbour</div>
      <div class="brand-mark__line">Developments</div>
      <div class="brand-mark__suffix">Pty Ltd</div>
    </div>
  </section>

</main>
</body>
</html>
```